Pregnancy and Fertility Information Website

Hello Designers,
I need a website which provide tips and information about healthy and happy pregnancy. My website name is Lorvin medical.

The website should provide all the information needed throughout pregnancy and beyond ranging from pregnancy tracking tools and articles about common pregnancy concerns and what to expect during pregnancy,etc.
The details about first trimester, second trimester and third trimester should be highlighted in the website.

Top Navigation
Home, Fertility, Pregnancy basics, Articles, Tips and News

I'm looking for a simple and clean design which involves captivating images and colors but it shouldn't be crowded. The design must be professional and modern. An easy to navigate layout is a must.

Green, violet, blue and light yellow colors are my favorites but i'm open to other options.

Any questions. Kindly ask

Industry/Entity Type

Medical

```html
<!DOCTYPE html>
<html lang="en">
<head>
<meta charset="utf-8">
<title>Lorvin medical — pregnancy and fertility</title>
<link href="https://fonts.googleapis.com/css2?family=Roboto:wght@400;500;700;900&display=swap" rel="stylesheet">
<style>
:root{
  --blue:#1f6db5;
  --blue-dark:#185c9c;
  --green:#4caf3c;
  --violet:#8c7fc0;
  --yellow:#f7c600;
  --orange:#f5a623;
  --ink:#2b2b2b;
  --muted:#7a7a7a;
  --line:#e2e2e2;
  --soft:#f3f3f3;
  --white:#ffffff;
}
*{box-sizing:border-box;margin:0;padding:0}
html,body{width:1200px;height:4412px;overflow:hidden}
body{font-family:"Roboto",Arial,sans-serif;color:var(--ink);background:var(--white);position:relative}
.abs{position:absolute}
.photo{position:absolute}

/* header */
.topbar{position:absolute;left:0;top:0;width:1200px;height:110px;background:var(--white);border-bottom:1px solid var(--line)}
.schedule{left:162px;top:4px;font-size:11px;color:var(--blue);font-weight:700}
.schedule span{color:var(--green)}
.contact{right:160px;top:2px;font-size:12px;color:var(--muted);display:flex;gap:22px;align-items:center}
.contact b{color:var(--blue);font-size:15px}
.brand{left:162px;top:38px;display:flex;align-items:center;gap:10px;font-size:20px;font-weight:700;color:var(--blue)}
.brand i{width:22px;height:22px;border-radius:50%;background:var(--green);display:block}
.nav{right:158px;top:48px;display:flex;gap:34px;font-size:15px;font-weight:500;color:var(--ink)}
.nav a{color:inherit;text-decoration:none;padding-bottom:10px}
.nav a.active{color:var(--blue);border-bottom:3px solid var(--blue)}

/* hero */
.hero{left:0;top:110px;width:1200px;height:596px;background:linear-gradient(180deg,#6fa6d6 0%,#9cc3e4 45%,#c9dded 62%,#4c7fa8 72%,#d9c8a6 100%)}
.hero-title{left:162px;top:212px;font-size:36px;font-weight:900;color:var(--white);letter-spacing:1px}
.hero-title span{color:var(--green)}
.hero-sub{left:162px;top:280px;width:720px;font-size:25px;font-weight:700;color:var(--white);line-height:1.35}
.btn-hero{left:162px;top:398px;width:256px;height:60px;border-radius:30px;background:var(--green);color:var(--white);font-size:17px;font-weight:700;display:flex;align-items:center;justify-content:center}

/* section headings */
.section-title{left:0;width:1200px;text-align:center;font-size:30px;font-weight:500;color:var(--ink)}
.divider{left:380px;width:440px;height:30px}
.intro{left:240px;width:720px;text-align:center;font-size:14px;line-height:1.55;color:var(--muted)}

/* know cards */
.know-card{width:276px;height:304px;border:1px solid var(--line);background:var(--white);padding:0 22px}
.know-card .icon{position:absolute;left:102px;top:-46px;width:104px;height:104px;border-radius:50%;background:var(--white);border:5px solid var(--yellow);display:flex;align-items:center;justify-content:center}
.know-card h3{margin-top:82px;font-size:17px;font-weight:500}
.know-card p{margin-top:18px;font-size:13px;line-height:1.55;color:var(--muted)}
.know-card .more{position:absolute;left:74px;bottom:26px;width:150px;height:38px;border:2px solid var(--green);border-radius:19px;font-size:14px;font-weight:500;display:flex;align-items:center;justify-content:center}
.know-card.featured{background:var(--blue);border-color:var(--blue);color:var(--white)}
.know-card.featured p{color:var(--white);font-weight:700}
.know-card.featured .icon{border-color:var(--green)}
.know-card.featured .more{background:var(--green);color:var(--white)}

/* doctor */
.about{left:0;top:1358px;width:1200px;height:307px;background:var(--blue)}
.about .portrait{left:160px;top:20px;width:256px;height:256px;border-radius:50%;border:6px solid var(--white);background:radial-gradient(circle at 50% 40%,#f1d9c5 0%,#e9eef3 55%,#c8d6e4 100%)}
.about h4{left:530px;top:68px;font-size:17px;font-weight:700;color:var(--white)}
.about p{left:530px;top:104px;width:520px;font-size:13.5px;line-height:1.55;color:var(--white);font-weight:500}

/* plan tabs */
.tabs{left:0;top:1886px;width:1200px;height:116px;border-top:1px solid var(--line);border-bottom:1px solid var(--line)}
.tab{position:absolute;top:0;width:147px;height:116px;text-align:center;font-size:13px;font-weight:500}
.tab svg{margin-top:12px}
.tab.active{border-bottom:4px solid var(--green);color:var(--green);background:#fafafa}
.tab span{display:block;margin-top:6px}
.plan-title{left:162px;top:2066px;font-size:22px;font-weight:500;padding-bottom:10px;border-bottom:2px solid var(--green)}
.plan-text{left:162px;top:2118px;width:640px;font-size:13px;line-height:1.6;color:var(--muted)}
.plan-photo{left:793px;top:2072px;width:236px;height:236px;border-radius:50%;background:linear-gradient(135deg,#dce7f1,#9fb8cf 60%,#e8edf2)}
.pill{height:44px;border-radius:22px;font-size:14px;font-weight:500;display:flex;align-items:center;justify-content:center}
.pill.outline{border:2px solid var(--green);color:var(--ink)}
.pill.solid{background:var(--green);color:var(--white)}

/* trimesters */
.tri{width:264px;height:400px}
.tri .bubble{position:absolute;left:0;top:54px;width:264px;height:264px;border-radius:50%;background:var(--soft)}
.tri .shape{position:absolute;left:32px;top:70px;width:200px;height:230px;border-radius:90px 90px 40px 40px;background:linear-gradient(180deg,#d3dbe4,#b7c4d2)}
.tri .tag{position:absolute;left:72px;width:120px;height:48px;color:var(--white);font-size:19px;font-weight:700;display:flex;align-items:center;justify-content:center}
.tri .tag.top{top:0}
.tri .tag.bottom{top:256px}
.tri .tag.top::after,.tri .tag.bottom::before{content:"";position:absolute;left:52px;border:8px solid transparent}
.tri .tag.top::after{bottom:-16px}
.tri .tag.bottom::before{top:-16px}
.t-blue{background:var(--blue)} .t-blue.top::after{border-top-color:var(--blue)} .t-blue.bottom::before{border-bottom-color:var(--blue)}
.t-violet{background:var(--violet)} .t-violet.top::after{border-top-color:var(--violet)} .t-violet.bottom::before{border-bottom-color:var(--violet)}
.t-orange{background:var(--orange)} .t-orange.top::after{border-top-color:var(--orange)} .t-orange.bottom::before{border-bottom-color:var(--orange)}
.tri .term{position:absolute;left:32px;top:342px;width:200px;height:48px;border-radius:24px;border:2px solid var(--green);font-size:19px;font-weight:500;display:flex;align-items:center;justify-content:center;background:var(--white)}
.tri .term.on{background:var(--green);color:var(--white)}
.tri .term.on::before{content:"";position:absolute;top:-16px;left:92px;border:8px solid transparent;border-bottom-color:var(--green)}
.tri .term sup{font-size:11px}

/* testimonials */
.testi{left:0;top:3087px;width:1200px;height:485px;background:var(--blue)}
.testi .photo{left:0;top:0;width:620px;height:485px;background:linear-gradient(110deg,#e9c9ae 0%,#f3dcc6 45%,#d9b696 75%,var(--blue) 100%)}
.testi h2{left:735px;top:92px;font-size:30px;font-weight:500;color:var(--white)}
.testi .tagline{left:712px;top:138px;font-size:17px;font-weight:700;color:var(--white)}
.testi .quote-mark{left:636px;top:184px;font-size:84px;color:var(--white);font-family:Georgia,serif;line-height:1}
.testi blockquote{left:684px;top:206px;width:370px;font-size:14px;line-height:1.6;color:var(--white);font-weight:700}
.testi .who{left:678px;top:367px;font-size:17px;font-weight:700;color:var(--white)}
.testi .role{left:678px;top:392px;font-size:13px;color:var(--white)}
.arrow-btn{width:36px;height:36px;display:flex;align-items:center;justify-content:center}

/* news */
.news{width:424px;height:172px;background:var(--soft);border:1px solid var(--line)}
.news .thumb{position:absolute;left:18px;top:22px;width:154px;height:128px}
.news h5{position:absolute;left:198px;top:24px;font-size:13px;font-weight:700}
.news .meta{position:absolute;left:198px;top:46px;font-size:9px;color:var(--blue);display:flex;gap:8px}
.news p{position:absolute;left:198px;top:66px;width:206px;font-size:11px;line-height:1.5;color:var(--muted)}
.news .read{position:absolute;left:198px;top:122px;width:66px;height:20px;border:1.5px solid var(--green);border-radius:10px;font-size:9px;font-weight:700;display:flex;align-items:center;justify-content:center}

/* footer */
.footer{left:0;top:4278px;width:1200px;height:134px;background:var(--blue);color:var(--white);font-size:12px;font-weight:700}
.footer nav{position:absolute;left:162px;top:60px;display:flex;gap:22px}
.footer .copy{position:absolute;right:160px;top:60px}
</style>
</head>
<body>

<header class="topbar">
  <div class="abs schedule">Schedule : <span>Saturday To Sunday - 9:00 AM To 5:00 PM, Sunday - 9:00 am To 2:00 PM</span></div>
  <div class="abs contact">
    <span>&#9993; info@lorvinmedical.com</span>
    <b>&#9742; 555 014 8220</b>
  </div>
  <div class="abs brand"><i></i>Lorvin medical</div>
  <nav class="abs nav">
    <a class="active" href="#">Home</a><a href="#">Fertility</a><a href="#">Pregnancy basics</a><a href="#">Articles</a><a href="#">Tips and News</a>
  </nav>
</header>

<section>
  <div class="photo hero" role="img" aria-label="Pregnant woman in a blue top standing on a beach under a cloudy sky"></div>
  <h1 class="abs hero-title">WELCOME TO THE <span>LORVIN</span> MEDICAL</h1>
  <p class="abs hero-sub">Your free and interactive tool for planning, pregnancy and early parenthood</p>
  <div class="abs btn-hero">Fix an Appointment with us</div>
</section>

<section>
  <h2 class="abs section-title" style="top:756px">Wanto to know</h2>
  <svg class="abs divider" style="top:802px" viewBox="0 0 440 30"><line x1="0" y1="15" x2="440" y2="15" stroke="#e6e6e6"/><circle cx="220" cy="15" r="12" fill="#fff" stroke="#dcdcdc" stroke-width="2"/></svg>
  <p class="abs intro" style="top:852px">Duae molestias excepturi sint occaecati cupiditate non provident, similique sunt in culpa qui officia deserunt mollitia animi, id est laborum et dolorum fuga</p>

  <article class="abs know-card" style="left:162px;top:996px">
    <div class="icon"><svg width="56" height="56" viewBox="0 0 56 56"><path d="M8 28 L28 10 L48 28" fill="none" stroke="#1f6db5" stroke-width="4"/><rect x="15" y="26" width="26" height="22" fill="none" stroke="#1f6db5" stroke-width="4"/><path d="M28 44 l-8-8 a4 4 0 0 1 8-4 a4 4 0 0 1 8 4z" fill="#4caf3c"/></svg></div>
    <h3>Healthy and Happy life</h3>
    <p>Duae molestias excepturi sint occaecati cupiditate non provident similique sunt in culpa qui officia deserunt mollitia animi, id</p>
    <div class="more">Read more</div>
  </article>
  <article class="abs know-card featured" style="left:462px;top:990px;height:310px">
    <div class="icon"><svg width="56" height="56" viewBox="0 0 56 56"><circle cx="28" cy="12" r="6" fill="#4caf3c"/><path d="M22 22 h12 l6 14 h-8 v14 h-8 v-14 h-8z" fill="#4caf3c"/></svg></div>
    <h3>PREGNANCY</h3>
    <p>Duae molestias excepturi sint occaecati cupiditate non provident, similique sunt in culpa qui officia deserunt mollitia animi, id</p>
    <div class="more">Read more</div>
  </article>
  <article class="abs know-card" style="left:762px;top:996px">
    <div class="icon"><svg width="56" height="56" viewBox="0 0 56 56"><rect x="12" y="10" width="32" height="40" rx="3" fill="none" stroke="#1f6db5" stroke-width="4"/><rect x="21" y="6" width="14" height="8" fill="#f7c600"/><line x1="19" y1="26" x2="37" y2="26" stroke="#4caf3c" stroke-width="3"/><line x1="19" y1="34" x2="37" y2="34" stroke="#4caf3c" stroke-width="3"/><line x1="19" y1="42" x2="31" y2="42" stroke="#4caf3c" stroke-width="3"/></svg></div>
    <h3>Prepregnancy Care</h3>
    <p>Duae molestias e fincepturi sint cupiditate, sint occaecati cupiditate non provident similique sunt in culpa qui officia deserunt mollitia animi, id</p>
    <div class="more">Read more</div>
  </article>
</section>

<section class="abs about">
  <div class="photo portrait" role="img" aria-label="Portrait of a smiling female doctor with a stethoscope"></div>
  <h4 class="abs">ABOUT OUR DR. MARA QUILL</h4>
  <p class="abs">Lorem ipsum dolor sit amet, consectetur adipiscing elit. Maecenas eget volutpat tellus. Mauris vestibulum, sapien ex posuere lacinia, erat nulla scelerisque tortor, et convallis turpis magna eu massa. In consequat</p>
</section>

<section>
  <h2 class="abs section-title" style="top:1708px">Our plan</h2>
  <svg class="abs divider" style="top:1754px" viewBox="0 0 440 30"><line x1="0" y1="15" x2="440" y2="15" stroke="#e6e6e6"/><circle cx="220" cy="15" r="12" fill="#fff" stroke="#dcdcdc" stroke-width="2"/></svg>
  <p class="abs intro" style="top:1802px">Duae molestias excepturi sint occaecati cupiditate non provident, similique sunt in culpa qui officia deserunt mollitia animi, id est laborum et dolorum fuga</p>

  <div class="abs tabs">
    <div class="tab" style="left:162px"><svg width="58" height="58" viewBox="0 0 58 58"><path d="M18 44 V20 a10 10 0 0 1 20 0 v10" fill="none" stroke="#1f6db5" stroke-width="4"/><circle cx="40" cy="36" r="6" fill="none" stroke="#4caf3c" stroke-width="4"/></svg><span>Health Care</span></div>
    <div class="tab active" style="left:309px"><svg width="58" height="58" viewBox="0 0 58 58"><circle cx="20" cy="14" r="6" fill="#1f6db5"/><circle cx="38" cy="14" r="6" fill="#8c7fc0"/><rect x="14" y="22" width="12" height="22" rx="4" fill="#1f6db5"/><rect x="32" y="22" width="12" height="22" rx="4" fill="#8c7fc0"/><path d="M29 52 l-5-5 a3 3 0 0 1 5-3 a3 3 0 0 1 5 3z" fill="#4caf3c"/></svg><span>Getting Pregnant</span></div>
    <div class="tab" style="left:456px"><svg width="58" height="58" viewBox="0 0 58 58"><circle cx="29" cy="29" r="22" fill="none" stroke="#f7c600" stroke-width="5"/><circle cx="31" cy="32" r="9" fill="#1f6db5"/></svg><span>Pregnancy</span></div>
    <div class="tab" style="left:603px"><svg width="58" height="58" viewBox="0 0 58 58"><circle cx="29" cy="29" r="22" fill="#f7c600"/><rect x="15" y="22" width="28" height="16" rx="3" fill="#fff"/><circle cx="29" cy="30" r="5" fill="#1f6db5"/></svg><span>Your First Scan</span></div>
    <div class="tab" style="left:750px"><svg width="58" height="58" viewBox="0 0 58 58"><circle cx="29" cy="20" r="10" fill="#f3c6a8"/><path d="M12 48 a17 14 0 0 1 34 0z" fill="#e04a4a"/><path d="M19 18 a10 10 0 0 1 20 0z" fill="#e04a4a"/></svg><span>Baby Birth</span></div>
    <div class="tab" style="left:897px"><svg width="58" height="58" viewBox="0 0 58 58"><circle cx="19" cy="20" r="10" fill="#f7c600"/><circle cx="39" cy="20" r="10" fill="#8c7fc0"/><rect x="9" y="32" width="20" height="16" rx="6" fill="#1f6db5"/><rect x="29" y="32" width="20" height="16" rx="6" fill="#4caf3c"/></svg><span>Baby Care</span></div>
  </div>

  <h3 class="abs plan-title">Getting Pregnant</h3>
  <p class="abs plan-text">Lorem ipsum dolor sit amet, consectetur adipiscing elit. Maecenas eget volutpat tellus. Mauris vestibulum, sapien ex posuere lacinia, erat nulla scelerisque tortor, et convallis turpis magna eu massa. In consequat ornare turpis a maximus. Praesent at sapien metus. Cras id augue consequat, ut aliquam magna vel, vestibulum mi sapien</p>
  <div class="photo plan-photo" role="img" aria-label="Couple in consultation with a doctor at a desk"></div>
  <div class="abs pill outline" style="left:162px;top:2265px;width:150px">Talk to us</div>
  <div class="abs pill solid" style="left:326px;top:2265px;width:182px">Make an Appointment</div>
</section>

<section>
  <h2 class="abs section-title" style="top:2378px">Learn about trimester</h2>
  <svg class="abs divider" style="top:2424px" viewBox="0 0 440 30"><line x1="0" y1="15" x2="440" y2="15" stroke="#e6e6e6"/><circle cx="220" cy="15" r="12" fill="#fff" stroke="#dcdcdc" stroke-width="2"/></svg>
  <p class="abs intro" style="top:2492px">Duae molestias excepturi sint occaecati cupiditate non provident, similique sunt in culpa qui officia deserunt mollitia animi, id est laborum et dolorum fuga</p>

  <div class="abs tri" style="left:156px;top:2590px">
    <div class="bubble"></div><div class="shape" role="img" aria-label="Silhouettes of pregnant women in early pregnancy"></div>
    <div class="tag top t-blue">1Week</div><div class="tag bottom t-blue">12Weeks</div>
    <div class="term on">1<sup>st</sup>&nbsp;Trimester!</div>
  </div>
  <div class="abs tri" style="left:466px;top:2590px">
    <div class="bubble"></div><div class="shape" role="img" aria-label="Silhouettes of pregnant women in mid pregnancy"></div>
    <div class="tag top t-violet">13Weeks</div><div class="tag bottom t-violet">27Weeks</div>
    <div class="term">2<sup>nd</sup>&nbsp;Trimester!</div>
  </div>
  <div class="abs tri" style="left:776px;top:2590px">
    <div class="bubble"></div><div class="shape" role="img" aria-label="Silhouettes of pregnant women in late pregnancy"></div>
    <div class="tag top t-orange">28Weeks</div><div class="tag bottom t-orange">To Birth</div>
    <div class="term">3<sup>rd</sup>&nbsp;Trimester!</div>
  </div>
</section>

<section class="abs testi">
  <div class="photo" role="img" aria-label="Mother holding a smiling baby"></div>
  <h2 class="abs">TESTMONIALS</h2>
  <div class="abs tagline">The expression can't tell a lie</div>
  <div class="abs quote-mark">&ldquo;</div>
  <blockquote class="abs">Lorem ipsum dolor sit amet, consectetur adipiscing elit. Donec ullamcorper accumsan. Morbi rutrum malesuada mi, nec ullamcorper ultrices</blockquote>
  <div class="abs who">Nell Harper</div>
  <div class="abs role">House wife</div>
  <div class="abs arrow-btn" style="left:900px;top:370px;background:#8fb3d6"><svg width="14" height="14" viewBox="0 0 14 14"><path d="M9 2 L4 7 L9 12" fill="none" stroke="#fff" stroke-width="2"/></svg></div>
  <div class="abs arrow-btn" style="left:942px;top:370px;background:#fff"><svg width="14" height="14" viewBox="0 0 14 14"><path d="M5 2 L10 7 L5 12" fill="none" stroke="#1f6db5" stroke-width="2"/></svg></div>
</section>

<section>
  <h2 class="abs section-title" style="top:3634px">Health news</h2>
  <svg class="abs divider" style="top:3680px" viewBox="0 0 440 30"><line x1="0" y1="15" x2="440" y2="15" stroke="#e6e6e6"/><circle cx="220" cy="15" r="12" fill="#fff" stroke="#dcdcdc" stroke-width="2"/></svg>
  <p class="abs intro" style="top:3732px">Duae molestias excepturi sint occaecati cupiditate non provident, similique sunt in culpa qui officia deserunt mollitia animi, id est laborum et dolorum fuga</p>

  <article class="abs news" style="left:162px;top:3814px">
    <div class="photo thumb" role="img" aria-label="Pregnant woman resting in bed" style="background:linear-gradient(135deg,#cfe2f2,#f1d6c4)"></div>
    <h5>Tips To Minimize Morning Sickness</h5>
    <div class="meta"><span>&#9679; Jan 12</span><span>&#9679; Posted by admin</span></div>
    <p>Lorem ipsum dolor sit amet, consectetur adipiscing elit. Maecenas eget volutpat tellus. Mauris vestibulum, sapien nec...</p>
    <div class="read">Read more</div>
  </article>
  <article class="abs news" style="left:620px;top:3814px">
    <div class="photo thumb" role="img" aria-label="Pregnant woman exercising with a ball" style="background:linear-gradient(135deg,#d8e6d3,#b9cde0)"></div>
    <h5>Great exercises during pregnancy</h5>
    <div class="meta"><span>&#9679; Jan 12</span><span>&#9679; Posted by admin</span></div>
    <p>Lorem ipsum dolor sit amet, consectetur adipiscing elit. Maecenas eget volutpat tellus. Mauris vestibulum...</p>
    <div class="read">Read more</div>
  </article>
  <article class="abs news" style="left:162px;top:4032px">
    <div class="photo thumb" role="img" aria-label="Pregnant woman holding a bowl of healthy food" style="background:linear-gradient(135deg,#e8ddd0,#c9d8b8)"></div>
    <h5>What To Eat During Pregnancy</h5>
    <div class="meta"><span>&#9679; Jan 12</span><span>&#9679; Posted by admin</span></div>
    <p>Lorem ipsum dolor sit amet, consectetur adipiscing elit. Maecenas eget volutpat tellus. Mauris vestibulum, sapien nec...</p>
    <div class="read">Read more</div>
  </article>
  <article class="abs news" style="left:620px;top:4032px">
    <div class="photo thumb" role="img" aria-label="Ultrasound scan on a monitor" style="background:linear-gradient(135deg,#c8d4e0,#8fa6bd)"></div>
    <h5>Premature birth risk</h5>
    <div class="meta"><span>&#9679; Jan 12</span><span>&#9679; Posted by admin</span></div>
    <p>Lorem ipsum dolor sit amet, consectetur adipiscing elit. Maecenas eget volutpat tellus. Mauris vestibulum...</p>
    <div class="read">Read more</div>
  </article>
</section>

<footer class="abs footer">
  <nav><span>Home</span><span>Fertility</span><span>Pregnancy basics</span><span>Articles</span><span>Tips and News</span></nav>
  <div class="copy">Copyright &copy; 2017 LORVIN MEDICAL All Rights Reserved</div>
</footer>

</body>
</html>
```